Header/Logo Redesign

****WE HAVE FOUND THE DESIGNER WHO WILL BE HANDLING THIS PROJECT. PLEASE DONT SUBMIT ANY MORE DESIGNS.****
We have been working with a Web/Logo Designer on a new header and logo for our site. We like some of it, but other things need changing.
Overall Look: We are looking for something that is professional, yet still fresh. Most business two business websites seem old fashinoned. The site we like most is www.tallyhaven.com.
Header Thoughts:
-We like the color at the top of the header. The light purple on the menu bar is a little dull though. It seems to be grayed out too much. Notice the pop that www.tallyhaven.com has. We need that pop.
-The fonts on the menu bar don't pop either. I don't know if it is because the font is bad or the thickness of the font is bad or what.
-We are not sold on the green color in the logo and header. It is pretty good, but maybe we can test other colors?
Logo Thoughts:
-I am not sold on the green color. It is pretty good, but maybe test it out with some other colors?
-The logo does not pop like the www.tallyhaven.com logo pops.
-We had started thinking about doing an owl as part of our name/logo or maybe some other type of animal. Look at the ideas I had sent our original graphic designer.
A. http://markvista.net/gallery/detail/842907 - i like that is simple, a little abstract, but I don't like that it is sort of evil.
B. http://markvista.net/gallery/detail/27514 - i like that is abstract.
C. http://pixelbrook.files.quillsite.net/2012/05/torvane4.jpg - i like the slightly abstract.
D. http://sketchlark.net/shots/718204-O-W-L - good - abrstract and slightly turned.
Target Market(s)
Sales and Marketing People - primarily a masculine audience in their 20s to 40s.
Industry/Entity Type
Business
Look and feel

```html
<!DOCTYPE html>
<html lang="en">
<head>
<meta charset="utf-8">
<title>Scout 208 — Header Studies</title>
<link rel="stylesheet" href="https://fonts.googleapis.com/css2?family=Ubuntu:wght@400;500;700&display=swap">
<style>
  :root {
    --page-bg: #ffffff;
    --top-bg: #3f3e66;
    --pill-bg: #4b4a78;
    --pill-text: #ffffff;
    --pill-text-soft: #d9d6f0;
    --brand-text: #ffffff;
    --search-bg: #f7f5f7;
    --search-text: #3c3a55;
    --search-icon: #2d3a6a;
    --divider: rgba(255, 255, 255, 0.28);
    --edge: #2b2a45;
  }
  * { box-sizing: border-box; margin: 0; padding: 0; }
  html, body {
    width: 1200px;
    height: 857px;
    overflow: hidden;
    background: var(--page-bg);
    font-family: "Ubuntu", sans-serif;
  }
  .board { position: relative; width: 1200px; height: 857px; }

  .header { position: absolute; left: 0; width: 1200px; height: 113px; }
  .header--violet  { top: 0;   --accent: #8a80d4; --nav-top: #3d3a78; --nav-bottom: #35336a; --tab-bg: #ffffff; --tab-text: #2d2b4f; --nav-text: #ffffff; --icon: #7f76d0; }
  .header--sky     { top: 238px; --accent: #45b3ee; --nav-top: #3db0f2; --nav-bottom: #6ccaf7; --tab-bg: rgba(255,255,255,0.35); --tab-text: #1f3550; --nav-text: #ffffff; --icon: var(--search-icon); }
  .header--magenta { top: 471px; --accent: #d53ed6; --nav-top: #a3009f; --nav-bottom: #f1d2f1; --tab-bg: rgba(255,255,255,0.35); --tab-text: #3a1d3c; --nav-text: #ffffff; --icon: var(--search-icon); }
  .header--slate   { top: 697px; --accent: #a9bd3a; --nav-top: #5d6a9a; --nav-bottom: #8492bd; --tab-bg: rgba(255,255,255,0.3); --tab-text: #2a2d48; --nav-text: #ffffff; --icon: var(--search-icon); }

  .header__top {
    position: absolute; left: 0; top: 0; width: 100%; height: 77px;
    background: var(--top-bg);
  }
  .header--sky .header__top,
  .header--magenta .header__top,
  .header--slate .header__top { border-top: 1px solid var(--edge); }

  .brand {
    position: absolute; left: 112px; top: 12px; height: 52px;
    display: flex; align-items: center; gap: 18px;
  }
  .brand__dot {
    width: 50px; height: 50px; border-radius: 50%;
    background: var(--accent);
  }
  .brand__name {
    font-weight: 700; font-size: 36px; letter-spacing: 0.5px;
    color: var(--brand-text);
  }

  .account {
    position: absolute; left: 787px; top: 0; width: 225px; height: 27px;
    background: var(--pill-bg);
    border-radius: 0 0 14px 14px;
    display: flex; align-items: center; justify-content: center; gap: 27px;
    font-size: 13px;
  }
  .account__link { color: var(--pill-text); text-decoration: none; }
  .account__link--soft { color: var(--pill-text-soft); }

  .nav {
    position: absolute; left: 0; top: 77px; width: 100%; height: 36px;
    background: linear-gradient(to bottom, var(--nav-top), var(--nav-bottom));
  }
  .header--violet .nav { box-shadow: 0 5px 8px rgba(80, 70, 160, 0.25); }
  .header--sky .nav,
  .header--magenta .nav,
  .header--slate .nav { border: 1px solid var(--edge); }

  .menu {
    position: absolute; left: 189px; top: 0; height: 100%;
    display: flex; list-style: none;
  }
  .menu__item {
    height: 100%; display: flex; align-items: center; justify-content: center;
    font-size: 15px; color: var(--nav-text);
    border-right: 1px solid var(--divider);
  }
  .menu__item--active { background: var(--tab-bg); color: var(--tab-text); width: 79px; border-right: none; }
  .menu__item--people { width: 88px; }
  .menu__item--companies { width: 116px; }
  .menu__item--downloads { width: 115px; }

  .search {
    position: absolute; left: 719px; top: 4px; width: 293px; height: 28px;
    background: var(--search-bg); border-radius: 14px;
    display: flex; align-items: center; padding: 0 12px;
    font-size: 13px; color: var(--search-text);
  }
  .search__icon { position: absolute; right: 12px; top: 4px; }
</style>
</head>
<body>
<main class="board">

  <header class="header header--violet">
    <div class="header__top">
      <div class="brand"><span class="brand__dot"></span><span class="brand__name">Scout 208</span></div>
      <nav class="account"><a class="account__link" href="#">Account Login</a><a class="account__link account__link--soft" href="#">Free Sign Up</a></nav>
    </div>
    <div class="nav">
      <ul class="menu">
        <li class="menu__item menu__item--active">New</li>
        <li class="menu__item menu__item--people">People</li>
        <li class="menu__item menu__item--companies">Companies</li>
        <li class="menu__item menu__item--downloads">Downloads</li>
      </ul>
      <div class="search">search
        <svg class="search__icon" width="20" height="20" viewBox="0 0 20 20"><circle cx="8" cy="8" r="6" fill="none" stroke="var(--icon)" stroke-width="2.6"/><line x1="12.5" y1="12.5" x2="18" y2="18" stroke="var(--icon)" stroke-width="3" stroke-linecap="round"/></svg>
      </div>
    </div>
  </header>

  <header class="header header--sky">
    <div class="header__top">
      <div class="brand"><span class="brand__dot"></span><span class="brand__name">Scout 208</span></div>
      <nav class="account"><a class="account__link" href="#">Account Login</a><a class="account__link account__link--soft" href="#">Free Sign Up</a></nav>
    </div>
    <div class="nav">
      <ul class="menu">
        <li class="menu__item menu__item--active">New</li>
        <li class="menu__item menu__item--people">People</li>
        <li class="menu__item menu__item--companies">Companies</li>
        <li class="menu__item menu__item--downloads">Downloads</li>
      </ul>
      <div class="search">search
        <svg class="search__icon" width="20" height="20" viewBox="0 0 20 20"><circle cx="8" cy="8" r="6" fill="none" stroke="var(--icon)" stroke-width="2.6"/><line x1="12.5" y1="12.5" x2="18" y2="18" stroke="var(--icon)" stroke-width="3" stroke-linecap="round"/></svg>
      </div>
    </div>
  </header>

  <header class="header header--magenta">
    <div class="header__top">
      <div class="brand"><span class="brand__dot"></span><span class="brand__name">Scout 208</span></div>
      <nav class="account"><a class="account__link" href="#">Account Login</a><a class="account__link account__link--soft" href="#">Free Sign Up</a></nav>
    </div>
    <div class="nav">
      <ul class="menu">
        <li class="menu__item menu__item--active">New</li>
        <li class="menu__item menu__item--people">People</li>
        <li class="menu__item menu__item--companies">Companies</li>
        <li class="menu__item menu__item--downloads">Downloads</li>
      </ul>
      <div class="search">search
        <svg class="search__icon" width="20" height="20" viewBox="0 0 20 20"><circle cx="8" cy="8" r="6" fill="none" stroke="var(--icon)" stroke-width="2.6"/><line x1="12.5" y1="12.5" x2="18" y2="18" stroke="var(--icon)" stroke-width="3" stroke-linecap="round"/></svg>
      </div>
    </div>
  </header>

  <header class="header header--slate">
    <div class="header__top">
      <div class="brand"><span class="brand__dot"></span><span class="brand__name">Scout 208</span></div>
      <nav class="account"><a class="account__link" href="#">Account Login</a><a class="account__link account__link--soft" href="#">Free Sign Up</a></nav>
    </div>
    <div class="nav">
      <ul class="menu">
        <li class="menu__item menu__item--active">New</li>
        <li class="menu__item menu__item--people">People</li>
        <li class="menu__item menu__item--companies">Companies</li>
        <li class="menu__item menu__item--downloads">Downloads</li>
      </ul>
      <div class="search">search
        <svg class="search__icon" width="20" height="20" viewBox="0 0 20 20"><circle cx="8" cy="8" r="6" fill="none" stroke="var(--icon)" stroke-width="2.6"/><line x1="12.5" y1="12.5" x2="18" y2="18" stroke="var(--icon)" stroke-width="3" stroke-linecap="round"/></svg>
      </div>
    </div>
  </header>

</main>
</body>
</html>
```